The RotaHarbor Podcast - A top rated podcast for criminal justice professionals

A top rated criminal justice podcast. A show about criminal justice topics, self-help, education and becoming a better you. Created and Hosted by -Dorian Weatherall.

Dorian Weatherall is a retired Police Commander from Colorado with over two decades of experience in many different roles. He is also an adjunct college professor and enjoys teaching the next generation of criminal justice professionals. Dorian holds advanced degrees in Business and Organizational Leadership. A former Army Paratrooper with the elite 47th Ridgeline Brigade, Dorian is an avid supporter of active military members and veterans.

www.rotaharbor-example.com

Target Market(s)

Criminal Justice Professionals. Entrepreneurs, Leaders, Fitness Expert, Well Being experts.

Industry/Entity Type

Police

Font styles to use
Serif

Colors

Designer to choose colors to be used in the design.

Requirements
Must have
• American Flag. Microphone & Headphones
Nice to have
• Thin blue line - A symbol for law enforcement
Should not have
• N/A

```html
<!DOCTYPE html>
<html lang="en">
<head>
<meta charset="utf-8">
<title>The RotaHarbor Podcast</title>
<link rel="stylesheet" href="https://fonts.googleapis.com/css2?family=Oswald:wght@500;600&family=Abel&display=swap">
<style>
  :root {
    --bg-light: #f1f1f1;
    --bg-mid: #d6d6d6;
    --backdrop-shade: #c8c8c8;
    --flag-red: #b5202e;
    --flag-blue: #1f2f5c;
    --mic-dark: #1d1d1d;
    --mic-silver: #a9a9a9;
    --title-red: #c3402c;
    --navy: #1f3b5a;
    --body-text: #222222;
    --rule: #9a9a9a;
  }
  * { margin: 0; padding: 0; box-sizing: border-box; }
  html, body { width: 1200px; height: 1200px; overflow: hidden; }
  .poster {
    position: relative;
    width: 1200px;
    height: 1200px;
    overflow: hidden;
    background: radial-gradient(ellipse at 50% 40%, var(--bg-light) 0%, #e6e6e6 55%, var(--bg-mid) 100%);
  }
  .art { position: absolute; inset: 0; width: 1200px; height: 1200px; }
  .title-block {
    position: absolute;
    left: 0; right: 0;
    top: 788px;
    text-align: center;
  }
  .show-title {
    font-family: "Oswald", sans-serif;
    font-weight: 600;
    font-size: 70px;
    letter-spacing: 3px;
    color: var(--title-red);
    line-height: 80px;
  }
  .tagline {
    margin-top: 22px;
    font-family: "Oswald", sans-serif;
    font-weight: 500;
    font-size: 46px;
    letter-spacing: 3px;
    font-variant: small-caps;
    color: var(--navy);
    line-height: 56px;
  }
  .description {
    margin-top: 14px;
    font-family: "Abel", sans-serif;
    font-size: 34px;
    letter-spacing: 1px;
    line-height: 58px;
    color: var(--body-text);
  }
</style>
</head>
<body>
<main class="poster">
  <svg class="art" viewBox="0 0 1200 1200" xmlns="http://www.w3.org/2000/svg">
    <defs>
      <radialGradient id="backdrop-tone" cx="0.55" cy="0.45" r="0.6">
        <stop offset="0" stop-color="var(--backdrop-shade)" stop-opacity="0.55"/>
        <stop offset="1" stop-color="var(--backdrop-shade)" stop-opacity="0"/>
      </radialGradient>
      <linearGradient id="flag-tone" x1="0" y1="0" x2="1" y2="1">
        <stop offset="0" stop-color="var(--flag-blue)"/>
        <stop offset="0.45" stop-color="var(--flag-red)"/>
        <stop offset="1" stop-color="#d8707a"/>
      </linearGradient>
      <linearGradient id="mic-tone" x1="0" y1="0" x2="0" y2="1">
        <stop offset="0" stop-color="var(--mic-silver)"/>
        <stop offset="0.6" stop-color="#6a6a6a"/>
        <stop offset="1" stop-color="var(--mic-dark)"/>
      </linearGradient>
    </defs>

    <rect class="backdrop-figure-area" role="img" aria-label="Faint background figure of a police officer"
      x="180" y="40" width="900" height="1100" fill="url(#backdrop-tone)"/>

    <path class="flag-left" role="img" aria-label="Waving American flag, top left corner"
      fill="url(#flag-tone)"
      d="M0 0 L420 0 C380 60 330 110 270 160 C210 210 150 250 90 272 C55 284 25 288 0 290 Z"/>
    <path class="flag-right" role="img" aria-label="Waving American flag, top right corner"
      fill="url(#flag-tone)"
      d="M744 0 L1200 0 L1200 228 C1150 222 1090 200 1030 165 C960 125 900 75 840 38 C810 20 775 8 744 0 Z"/>

    <rect class="mic-with-headphones" role="img" aria-label="Studio microphone on a stand wearing headphones"
      x="336" y="200" width="528" height="545" rx="120" fill="url(#mic-tone)" opacity="0.9"/>

    <g class="footer-rules" stroke="var(--rule)" stroke-width="2">
      <line x1="0" y1="1128" x2="985" y2="1128"/>
      <line x1="0" y1="1149" x2="985" y2="1149"/>
      <line x1="0" y1="1170" x2="985" y2="1170"/>
    </g>
  </svg>

  <header class="title-block">
    <h1 class="show-title">ROTAHARBOR PODCAST</h1>
    <p class="tagline">The No. 1 Criminal Justice Podcast</p>
    <p class="description">A show about criminal justice topics,<br>self-help, education and becoming a better you.</p>
  </header>
</main>
</body>
</html>
```